Business Card Design for Law firm - already have logo

Now that we have a logo, we need a business card design - our logo is attached -it is salaryman font if that helps - we would like a file that can be uploaded to kellumo (www.kellumo.com) using the logo and with the following information on it:
Dunmore Law Firm, P.C.
Felix Dunmore, Esq.
6718 NE 19th Ave.
Portland, OR 97284
971.555.0142 phone
971.555.0187 fax
fel@dunmore.net
Skype: feldunmore
Google talk: felix.dunmore@quillmail.com
Target Market(s)
our business cards are distributed to corporate executives, technology professionals and healthcare providers
Industry/Entity Type
Business
Look and feel

```html
<!DOCTYPE html>
<html lang="en">
<head>
<meta charset="utf-8">
<title>Dunmore Law Firm – Business Card</title>
<link rel="stylesheet" href="https://fonts.googleapis.com/css2?family=Roboto+Condensed:wght@400;700&display=swap">
<style>
  :root {
    --page-bg: #e4e4e4;
    --card-bg: #3a3a3a;
    --rule: #1f1f1f;
    --icon: #202020;
    --text: #ffffff;
  }
  * { margin: 0; padding: 0; box-sizing: border-box; }
  html, body { width: 1200px; height: 1000px; overflow: hidden; }
  body {
    background: var(--page-bg);
    font-family: "Roboto Condensed", "Arial Narrow", sans-serif;
    color: var(--text);
    position: relative;
  }
  .card {
    position: absolute;
    left: 82px; top: 204px;
    width: 1035px; height: 593px;
    background: var(--card-bg);
  }
  .wordmark {
    position: absolute;
    left: 38px; top: 226px;
    width: 570px; height: 140px;
  }
  .wordmark text {
    font-family: "Roboto Condensed", "Arial Narrow", sans-serif;
    font-weight: 400;
    font-size: 74px;
    fill: var(--text);
  }
  .details {
    position: absolute;
    left: 653px; top: 0;
    right: 0; height: 100%;
  }
  .holder-name {
    position: absolute; top: 78px;
    font-size: 40px; font-weight: 700; letter-spacing: 0.3px;
    white-space: nowrap;
  }
  .holder-name .suffix { font-size: 28px; font-weight: 400; letter-spacing: 0; }
  .holder-email { position: absolute; top: 124px; font-size: 28px; }
  .rule {
    position: absolute; left: 0; right: 0;
    height: 3px; background: var(--rule);
  }
  .rule.top { top: 226px; }
  .rule.bottom { top: 357px; }
  .firm-address {
    position: absolute; top: 238px;
    font-size: 28px; line-height: 38px; font-style: normal;
  }
  .contact-list {
    position: absolute; top: 396px;
    list-style: none;
  }
  .contact-list li {
    display: flex; align-items: center;
    height: 40px; font-size: 27px;
  }
  .contact-list svg { width: 29px; height: 29px; margin-right: 14px; flex: none; }
  .contact-list svg .glyph-bg { fill: var(--icon); }
  .contact-list svg .glyph { fill: var(--card-bg); }
</style>
</head>
<body>
  <main class="card">
    <svg class="wordmark" viewBox="0 0 570 140" role="img" aria-label="Dunmore">
      <text x="2" y="100" textLength="564" lengthAdjust="spacing">DUNMORE</text>
    </svg>

    <section class="details">
      <h1 class="holder-name">FELIX DUNMORE<span class="suffix">, Esq.</span></h1>
      <p class="holder-email">fel@dunmore.net</p>

      <div class="rule top"></div>
      <address class="firm-address">
        Dunmore Law Firm, P.C.<br>
        6718 NE 19th Ave.<br>
        Portland, OR 97284
      </address>
      <div class="rule bottom"></div>

      <ul class="contact-list">
        <li>
          <svg viewBox="0 0 29 29" aria-label="Phone">
            <rect class="glyph-bg" width="29" height="29" rx="5"/>
            <path class="glyph" d="M9 6.5c1-.6 2-.3 2.5.6l1.6 3c.4.8.2 1.6-.5 2.1l-1 .8c.9 2 2.5 3.6 4.5 4.5l.8-1c.5-.7 1.3-.9 2.1-.5l3 1.6c.9.5 1.2 1.5.6 2.5l-1 1.5c-.8 1.1-2.2 1.5-3.5 1-5.3-1.9-9.1-5.7-11-11-.5-1.3-.1-2.7 1-3.5z"/>
          </svg>
          971.555.0142
        </li>
        <li>
          <svg viewBox="0 0 29 29" aria-label="Fax">
            <rect class="glyph-bg" x="7" y="2" width="15" height="7" rx="1"/>
            <rect class="glyph-bg" x="1" y="10" width="27" height="12" rx="3"/>
            <rect class="glyph-bg" x="7" y="18" width="15" height="10" rx="1"/>
            <rect class="glyph" x="9" y="20" width="11" height="6"/>
          </svg>
          971.555.0187
        </li>
        <li>
          <svg viewBox="0 0 29 29" aria-label="Chat handle">
            <circle class="glyph-bg" cx="14.5" cy="14.5" r="13.5"/>
          </svg>
          feldunmore
        </li>
        <li>
          <svg viewBox="0 0 29 29" aria-label="Messaging address">
            <circle class="glyph-bg" cx="14.5" cy="14.5" r="13.5"/>
          </svg>
          felix.dunmore@quillmail.com
        </li>
      </ul>
    </section>
  </main>
</body>
</html>
```